Specialist Executive Search firm needs new MS Word template(and other templates to match eventually)

Larkfield Associates a boutique Executive Search and Recruitment firm, recruiting senior specialist advisors in the fields of Audit, Advisory, Tax Accounting, Corporate Finance and Law. The majority of our clients are professional services firms, i.e. Accounting firms and Law firms.

The ‘Research List / Market Map’ document we currently use to produce and then present to clients is a "long list" of candidates or prospective target candidates. It is a bit dated, and the formatting can be fiddly. So we would like someone to freshen it up and simplify it so that is functions much more effectively as a usable, consistent Template and it needs to be in MS Word. We are looking for something simple and contemporary, but professional, given the nature of our clients - usually Managing Partners or very Senior Partners - in Accounting and Law firms. We need it to be easy to use, so that we can just copy and paste information into it without the formatting requiring constant adjustment and checking.

The "usual" sequence of the document:

- Cover page - includes the name of the company we are sending it to, the role we are recruiting for, and a sketch of the city the role is in (or similar other sketch). The Larkfield Associates brand is also featured.
- Confidentiality summary page,
- Table of contents - we would like this to be automated so that page numbers adjusted automatically to be accurate with contents page
- Project summary - usually 1 to 2 pages summarising the purpose of the project and the content of the document
- "Highlighted Candidates" page, which are targets / candidates we think are likely of particular interest to our client.
- Then a page or number of pages (depending on the nature of the search, this is sometimes up to 5 to 6 pages for each and every firm….with an average of 3/4 individuals per page. Other times, it may be just one individual per employer/firm) listed by firm with the following details of each candidate:
- Photo of target individual
- Name of individual
- Job title
- Location
- Summary of the individual and their experience, which can be between 1-2 paragraphs.

We are open to suggestions with respect to the above, i.e. improved format / layout / order of information.

We currently group target candidates by the firm that currently employs each. Each firm has the heading and we like them grouped this way, as do our clients as it assists with seeking feedback / market information from various stakeholders inside the client. We tend to group very large firms (Tbr, HLSW, Fenwrick, QO) at the beginning of each market document, followed by large international mid tier firms, followed by quality boutiques and smaller firms. Whilst it can vary somewhat, generally speaking the larger firms are comprised of a larger number of potential targets than smaller firms. For obvious reasons.

I have attached an example of what we currently have, but please bear in mind this is a mock up for confidentiality reasons. I haven't included the confidentiality summary page, or the project summary either. Ideally for integration purposes, and to make it simpler to copy data from our CRM system and paste into the document, there will be a hidden table for the candidate information.

We also want a new font, as the one we have (DIN) needs to be downloaded by each user and if we send the document in MS Word format, the formatting can be totally unreadable to the recipient or at the very least can impact the layout and format. So perhaps a simple font that we can use as part of our brand, but that still looks smart and contemporary.

Once we finalise this word template, we will need to match it with our other proposal documents, terms of business, powerpoint templates etc, and we also need to refresh/redo our website.

I only work two days per week so it's a long time between me reviewing designs, and discussing with the Partners of the business.

Professional services firms, Director and Partner level

Recruitment

• Currently use DIN but keen for a different signature font to suit

• Must be simple to copy and paste text from our other system, and our business colours which are dark brown and dark red - RGB codes to come shortly

```html
<!DOCTYPE html>
<html lang="en">
<head>
<meta charset="utf-8">
<title>Larkfield Associates – Research List Template</title>
<link rel="stylesheet" href="https://fonts.googleapis.com/css2?family=Montserrat:wght@300;700;800&family=Raleway:ital,wght@0,300;0,400;0,600;0,700;1,400&display=swap">
<style>
  :root {
    --stage: #808080;
    --paper: #ffffff;
    --brown: #5a2319;
    --red: #c0272d;
    --ink: #3a3a3a;
    --soft-ink: #6b6b6b;
    --numeral: #c9c9c9;
    --tile: #f1f1f1;
    --rule: #dcdcdc;
    --amber: #f2b21c;
    --green: #2fa84f;
  }
  * { margin: 0; padding: 0; box-sizing: border-box; }
  html, body { width: 686px; height: 1200px; overflow: hidden; }
  body { position: relative; background: var(--stage); font-family: "Raleway", Arial, sans-serif; color: var(--ink); }

  .page { position: absolute; width: 295px; height: 221px; background: var(--paper); box-shadow: 0 6px 10px rgba(0,0,0,.28); overflow: hidden; }
  .col-left { left: 37px; } .col-right { left: 354px; }
  .row-1 { top: 116px; } .row-2 { top: 366px; } .row-3 { top: 614px; } .row-4 { top: 863px; }

  .brand { position: absolute; font-family: "Raleway", Arial, sans-serif; font-weight: 700; color: var(--brown); line-height: 1; white-space: nowrap; }
  .brand-header { top: 14px; right: 16px; font-size: 6.5px; }

  .page-title { position: absolute; left: 19px; top: 12px; font-family: "Montserrat", Arial, sans-serif; font-weight: 800; font-size: 12px; line-height: 1.3; color: var(--ink); letter-spacing: .2px; }
  .page-title::after { content: ""; display: block; width: 35px; height: 1px; background: var(--red); margin-top: 2px; }
  .page-title.firm { font-family: "Montserrat", Arial, sans-serif; color: var(--brown); font-size: 10.5px; }

  .footer { position: absolute; left: 11px; right: 10px; bottom: 8px; border-top: .5px solid var(--rule); padding-top: 2px; height: 9px; }
  .footer .page-no { position: absolute; left: 0; top: 4px; font-size: 3px; color: var(--soft-ink); }
  .footer .offices { position: absolute; right: 0; top: 2px; font-size: 2.8px; text-align: right; line-height: 1.35; color: var(--ink); }
  .footer .web { color: var(--red); display: block; }

  /* Cover */
  .cover-art { position: absolute; left: 8px; top: 8px; width: 279px; height: 146px; background: linear-gradient(180deg, #efe8ea 0%, #e4d6da 45%, #c9d3cf 70%, #d9dedd 100%); }
  .cover-title { position: absolute; left: 18px; top: 164px; font-family: "Montserrat", Arial, sans-serif; font-weight: 800; font-size: 11px; color: var(--brown); }
  .cover-title::after { content: ""; display: block; width: 35px; height: 1px; background: var(--red); margin-top: 1px; }
  .cover-meta { position: absolute; left: 18px; font-size: 5px; font-weight: 600; color: var(--ink); }
  .cover-role { top: 185px; } .cover-client { top: 196px; }
  .cover-date { position: absolute; left: 18px; top: 206px; font-size: 5px; font-style: italic; color: var(--red); }
  .cover-brand { top: 172px; right: 11px; font-size: 9px; }
  .cover-offices { position: absolute; right: 11px; top: 202px; font-size: 2.8px; text-align: right; line-height: 1.35; }
  .cover-offices .web { color: var(--red); display: block; }

  /* Contents */
  .toc-title { position: absolute; left: 11px; top: 17px; font-family: "Montserrat", Arial, sans-serif; font-weight: 800; font-size: 10.5px; color: var(--brown); }
  .toc { position: absolute; left: 11px; right: 12px; top: 37px; list-style: none; }
  .toc li { display: flex; align-items: baseline; font-size: 4.4px; height: 8.3px; color: var(--ink); }
  .toc .leader { flex: 1; border-bottom: .5px dotted #999; margin: 0 1px; transform: translateY(-1px); }

  /* Summary */
  .body-copy { position: absolute; left: 22px; right: 21px; top: 50px; font-size: 4.55px; line-height: 1.38; text-align: justify; color: var(--ink); }
  .body-copy p { margin-bottom: 4px; }
  .body-copy ul { list-style: none; margin-bottom: 4px; }
  .body-copy li { position: relative; padding-left: 9px; margin-bottom: 4.5px; }
  .body-copy li::before { content: "•"; position: absolute; left: 0; }

  /* Highlights */
  .callout { position: absolute; left: 19px; top: 57px; width: 257px; height: 30px; background: var(--red); color: #fff; font-weight: 600; font-size: 5.4px; line-height: 1.3; padding: 8px 7px 0; }
  .highlight { position: absolute; width: 120px; display: flex; }
  .highlight .num { font-family: "Montserrat", Arial, sans-serif; font-weight: 700; font-size: 12px; color: var(--numeral); width: 26px; line-height: 1; }
  .highlight h3 { font-size: 5px; font-weight: 700; color: var(--ink); margin-bottom: 1.5px; }
  .highlight p { font-size: 4.5px; font-weight: 300; line-height: 1.3; color: var(--ink); }

  /* Firm grid */
  .firm-tile { position: absolute; width: 82px; height: 41px; background: var(--tile); font-family: "Montserrat", Arial, sans-serif; font-weight: 700; font-size: 5.7px; color: var(--ink); padding: 30px 0 0 20px; }

  /* Candidate cards */
  .card { position: absolute; background: var(--tile); }
  .avatar { position: absolute; border-radius: 50%; border: 1.3px solid var(--red); background: linear-gradient(180deg, #d8d8d8, #9a9a9a); }
  .status { position: absolute; width: 5px; height: 5px; border-radius: 50%; border: .6px solid #fff; }
  .status.red { background: var(--red); } .status.green { background: var(--green); } .status.amber { background: var(--amber); }
  .cand-name { font-family: "Montserrat", Arial, sans-serif; font-weight: 700; font-size: 4.3px; color: var(--ink); }
  .cand-title { font-size: 4.3px; color: var(--red); margin-top: 2px; }
  .cand-loc { font-size: 4.3px; font-style: italic; color: var(--ink); margin-top: 2px; }
  .cand-bio { font-size: 2.6px; line-height: 1.3; color: var(--ink); }
  .cand-bio p { margin-bottom: 1.5px; }

  .card.grid { width: 127px; height: 72px; }
  .card.grid .avatar { left: 12px; top: 6px; width: 13px; height: 13px; }
  .card.grid .status { left: 12px; top: 15px; }
  .card.grid .cand-head { position: absolute; left: 46px; top: 12px; }
  .card.grid .cand-head > * { margin-top: 1px; }
  .card.grid .cand-bio { position: absolute; left: 12px; right: 9px; top: 38px; }

  .card.row { left: 16px; width: 261px; height: 47px; }
  .card.row .avatar { left: 24px; top: 8px; width: 15px; height: 15px; }
  .card.row .status { left: 24px; top: 19px; }
  .card.row .cand-head { position: absolute; left: 51px; top: 9px; }
  .card.row .cand-head .cand-name { font-size: 5px; }
  .card.row .cand-head .cand-title, .card.row .cand-head .cand-loc { font-size: 5px; margin-top: 4px; }
  .card.row .cand-bio { position: absolute; left: 110px; right: 14px; top: 9px; font-size: 2.8px; }
</style>
</head>
<body>

<!-- Cover -->
<section class="page col-left row-1">
  <div class="cover-art" role="img" aria-label="Pale sketch of the Sydney harbour skyline and opera house"></div>
  <h1 class="cover-title">REPORT</h1>
  <p class="cover-meta cover-role">Partner Corporate Tax – Sydney</p>
  <p class="cover-meta cover-client">Prepared for “Client”</p>
  <p class="cover-date">9 March 2020</p>
  <div class="brand cover-brand">Larkfield Associates</div>
  <p class="cover-offices">London | Dubai | Melbourne | St. Helier | Sydney<span class="web">www.larkfieldassociates.net</span></p>
</section>

<!-- Contents -->
<section class="page col-right row-1">
  <h2 class="toc-title">Table of Contents</h2>
  <ol class="toc">
    <li>Summary<span class="leader"></span>2</li>
    <li>Summary<span class="leader"></span>3</li>
    <li>Contents<span class="leader"></span>4</li>
    <li>Notable Individuals/Firms<span class="leader"></span>5</li>
    <li>Notable Individuals/Firms<span class="leader"></span>6</li>
    <li>Fenwrick<span class="leader"></span>7</li>
    <li>QO<span class="leader"></span>8</li>
  </ol>
  <footer class="footer"><span class="page-no">9</span><p class="offices">London | Dubai | Melbourne | St. Helier | Sydney<span class="web">www.larkfieldassociates.net</span></p></footer>
</section>

<!-- Summary 1 -->
<section class="page col-left row-2">
  <h2 class="page-title">SUMMARY</h2>
  <div class="brand brand-header">Larkfield Associates</div>
  <div class="body-copy">
    <p>Lorem ipsum is simply dummy text of the printing and typesetting industry. Lorem ipsum has been the industry's standard dummy text ever since the 1500s, when an unknown printer took a galley of type and scrambled it to make a type specimen book. It has survived not only five centuries, but also the leap into electronic typesetting, remaining essentially unchanged. It was popularised in the 1960s with the release of sheets containing Lorem Ipsum passages, and more recently with desktop publishing software including versions of Lorem Ipsum.</p>
    <p>Contrary to popular belief, Lorem Ipsum is not simply random text. It has roots in a piece of classical Latin literature from 45 BC, making it over 2000 years old. Sed ut perspiciatis unde omnis iste natus error sit voluptatem accusantium doloremque laudantium, totam rem aperiam, eaque ipsa quae ab illo inventore veritatis et quasi architecto beatae vitae dicta sunt explicabo. Nemo enim ipsam voluptatem quia voluptas sit aspernatur aut odit aut fugit, sed quia consequuntur magni dolores eos qui ratione. The first line of Lorem Ipsum, "Lorem ipsum dolor sit amet..", comes from a line in section 1.10.32.</p>
    <p>The standard chunk of Lorem Ipsum used since the 1500s is reproduced below for those interested. Sections 1.10.32 and 1.10.33 are also reproduced in their exact original form, accompanied by English versions from a later translation.</p>
    <p>It is a long established fact that a reader will be distracted by the readable content of a page when looking at its layout. The point of using Lorem Ipsum is that it has a more-or-less normal distribution of letters, as opposed to using 'Content here, content here'.</p>
  </div>
  <footer class="footer"><span class="page-no">3</span><p class="offices">London | Dubai | Melbourne | St. Helier | Sydney<span class="web">www.larkfieldassociates.net</span></p></footer>
</section>

<!-- Summary 2 -->
<section class="page col-right row-2">
  <h2 class="page-title">SUMMARY</h2>
  <div class="brand brand-header">Larkfield Associates</div>
  <div class="body-copy" style="top:48px">
    <ul>
      <li>Lorem Ipsum is simply dummy text of the printing and typesetting industry.</li>
      <li>Lorem Ipsum has been the industry's standard dummy text ever since the 1500s, when an unknown printer took a galley of type and scrambled it to make a type specimen book.</li>
      <li>It has survived not only five centuries, but also the leap into electronic typesetting, remaining essentially unchanged.</li>
      <li>It was popularised in the 1960s with the release of sheets containing Lorem Ipsum passages, and more recently with desktop publishing software including versions of Lorem Ipsum.</li>
    </ul>
    <p>Contrary to popular belief, Lorem Ipsum is not simply random text. It has roots in a piece of classical Latin literature from 45 BC, making it over 2000 years old. Sed ut perspiciatis unde omnis iste natus error sit voluptatem accusantium doloremque laudantium, totam rem aperiam, eaque ipsa quae ab illo inventore veritatis et quasi architecto beatae vitae dicta sunt explicabo. Nemo enim ipsam voluptatem quia voluptas sit aspernatur aut odit aut fugit. The first line of Lorem Ipsum, "Lorem ipsum dolor sit amet..", comes from a line in section 1.10.32.</p>
    <p>The standard chunk of Lorem Ipsum used since the 1500s is reproduced below for those interested. Sections 1.10.32 and 1.10.33 are also reproduced in their exact original form, accompanied by English versions from a later translation.</p>
  </div>
  <footer class="footer"><span class="page-no">4</span><p class="offices">London | Dubai | Melbourne | St. Helier | Sydney<span class="web">www.larkfieldassociates.net</span></p></footer>
</section>

<!-- Highlights -->
<section class="page col-left row-3">
  <h2 class="page-title">NOTABLE<br>INDIVIDUALS / FIRMS</h2>
  <div class="brand brand-header">Larkfield Associates</div>
  <p class="callout">We have highlighted a few individuals and firms that we believe are worth exploring further to determine their level of appropriateness and potential interest in CLIENT:</p>
  <div class="highlight" style="left:22px;top:106px"><span class="num">01</span><div><h3>Heading here</h3><p>Lorem Ipsum is simply dummy text of the printing and typesetting industry.</p></div></div>
  <div class="highlight" style="left:22px;top:141px"><span class="num">02</span><div><h3>Heading here</h3><p>Lorem Ipsum is simply dummy text of the printing and typesetting industry.</p></div></div>
  <div class="highlight" style="left:22px;top:176px"><span class="num">03</span><div><h3>Heading here</h3><p>Lorem Ipsum is simply dummy text of the printing and typesetting industry.</p></div></div>
  <div class="highlight" style="left:161px;top:107px"><span class="num">04</span><div><h3>Heading here</h3><p>Lorem Ipsum is simply dummy text of the printing and typesetting industry.</p></div></div>
  <div class="highlight" style="left:161px;top:142px"><span class="num">05</span><div><h3>Heading here</h3><p>Lorem Ipsum is simply dummy text of the printing and typesetting industry.</p></div></div>
  <div class="highlight" style="left:161px;top:177px"><span class="num">06</span><div><h3>Heading here</h3><p>Lorem Ipsum is simply dummy text of the printing and typesetting industry.</p></div></div>
  <footer class="footer"><span class="page-no">5</span><p class="offices">London | Dubai | Melbourne | St. Helier | Sydney<span class="web">www.larkfieldassociates.net</span></p></footer>
</section>

<!-- Firm grid -->
<section class="page col-right row-3">
  <h2 class="page-title">NOTABLE<br>INDIVIDUALS / FIRMS</h2>
  <div class="brand brand-header">Larkfield Associates</div>
  <div class="firm-tile" style="left:20px;top:59px">Lorem Ipsum</div>
  <div class="firm-tile" style="left:106px;top:59px">Lorem Ipsum</div>
  <div class="firm-tile" style="left:193px;top:59px">Lorem Ipsum</div>
  <div class="firm-tile" style="left:20px;top:106px">Lorem Ipsum</div>
  <div class="firm-tile" style="left:106px;top:106px">Lorem Ipsum</div>
  <div class="firm-tile" style="left:193px;top:106px">Lorem Ipsum</div>
  <div class="firm-tile" style="left:20px;top:152px">Lorem Ipsum</div>
  <div class="firm-tile" style="left:106px;top:152px">Lorem Ipsum</div>
  <div class="firm-tile" style="left:193px;top:152px">Lorem Ipsum</div>
  <footer class="footer"><span class="page-no">6</span><p class="offices">London | Dubai | Melbourne | St. Helier | Sydney<span class="web">www.larkfieldassociates.net</span></p></footer>
</section>

<!-- Fenwrick -->
<section class="page col-left row-4">
  <h2 class="page-title firm" style="left:21px;top:15px">Fenwrick</h2>
  <div class="brand brand-header" style="top:18px;right:20px">Larkfield Associates</div>

  <article class="card grid" style="left:17px;top:46px">
    <div class="avatar" role="img" aria-label="Candidate A portrait"></div><span class="status red"></span>
    <div class="cand-head"><p class="cand-name">CANDIDATE A</p><p class="cand-title">Partner</p><p class="cand-loc">Sydney</p></div>
    <div class="cand-bio"><p>Candidate A has been a Tax Partner with the firm since 2005, having joined as a graduate in 1993. She is a financial services specialist.</p><p>Candidate A holds a Bachelor of Commerce and a Masters of Taxation.</p></div>
  </article>
  <article class="card grid" style="left:151px;top:46px">
    <div class="avatar" role="img" aria-label="Candidate B portrait"></div><span class="status green"></span>
    <div class="cand-head"><p class="cand-name">CANDIDATE B</p><p class="cand-title">Partner</p><p class="cand-loc">Sydney</p></div>
    <div class="cand-bio"><p>Candidate B is a partner with over 13 years of experience as a tax adviser to investment management, infrastructure, private equity and real estate clients.</p><p>He advises on fund establishment, acquisitions, due diligence, structuring and ongoing compliance.</p></div>
  </article>
  <article class="card grid" style="left:17px;top:124px">
    <div class="avatar" role="img" aria-label="Candidate C portrait"></div><span class="status amber"></span>
    <div class="cand-head"><p class="cand-name">CANDIDATE C</p><p class="cand-title">Partner</p><p class="cand-loc">Sydney</p></div>
    <div class="cand-bio"><p>Candidate C is a Partner in the tax division in Sydney and joined in 2013.</p><p>He has broad experience in international accounting and law firms.</p><p>He mainly advises large corporate clients on infrastructure, M&amp;A and capital management.</p></div>
  </article>
  <article class="card grid" style="left:151px;top:124px">
    <div class="avatar" role="img" aria-label="Candidate D portrait"></div><span class="status red"></span>
    <div class="cand-head"><p class="cand-name">CANDIDATE D</p><p class="cand-title">Partner</p><p class="cand-loc">Sydney</p></div>
    <div class="cand-bio"><p>Candidate B is a partner with over 13 years of experience as a tax adviser to investment management, infrastructure, private equity and real estate clients.</p><p>He advises on fund establishment, acquisitions, due diligence, structuring and ongoing compliance.</p></div>
  </article>
  <footer class="footer"><span class="page-no" style="left:10px">7</span><p class="offices">London | Dubai | Melbourne | St. Helier | Sydney<span class="web">www.larkfieldassociates.net</span></p></footer>
</section>

<!-- QO -->
<section class="page col-right row-4">
  <h2 class="page-title firm" style="left:21px;top:15px">QO</h2>
  <div class="brand brand-header" style="top:18px;right:20px">Larkfield Associates</div>

  <article class="card row" style="top:40px">
    <div class="avatar" role="img" aria-label="Candidate A portrait"></div><span class="status red"></span>
    <div class="cand-head"><p class="cand-name">CANDIDATE A</p><p class="cand-title">Partner</p><p class="cand-loc">Sydney</p></div>
    <div class="cand-bio"><p>Candidate A has been a Tax Partner with the firm since 2005, having joined as a graduate in 1993. She is a financial services specialist.</p><p>Candidate A holds a Bachelor of Commerce and a Masters of Taxation.</p></div>
  </article>
  <article class="card row" style="top:93px">
    <div class="avatar" role="img" aria-label="Candidate B portrait"></div><span class="status green"></span>
    <div class="cand-head"><p class="cand-name">CANDIDATE B</p><p class="cand-title">Partner</p><p class="cand-loc">Sydney</p></div>
    <div class="cand-bio"><p>Candidate B is a partner with over 13 years of experience as a tax adviser to investment management, infrastructure, private equity and real estate clients.</p><p>He advises on fund establishment, acquisitions, due diligence, structuring and ongoing compliance.</p></div>
  </article>
  <article class="card row" style="top:146px">
    <div class="avatar" role="img" aria-label="Candidate C portrait"></div><span class="status amber"></span>
    <div class="cand-head"><p class="cand-name">CANDIDATE A</p><p class="cand-title">Partner</p><p class="cand-loc">Sydney</p></div>
    <div class="cand-bio"><p>Candidate C is a Partner in the tax division in Sydney and joined in 2013.</p><p>He has broad experience in international accounting and law firms.</p><p>He mainly advises large corporate clients on infrastructure, M&amp;A and capital management.</p></div>
  </article>
  <footer class="footer"><span class="page-no" style="left:10px">8</span><p class="offices">London | Dubai | Melbourne | St. Helier | Sydney<span class="web">www.larkfieldassociates.net</span></p></footer>
</section>

</body>
</html>
```